Business Card Design

We need a business card design for our new expansion based in Bloomfield Hills, Michigan. Our company is Quiet Harbor Institute & Wellness Center. Our Academy teaches individuals of all ages and professions to live from their soul. We teach intuitive development, meditation and mindfulness; shamanic healing. And ourr healing center provides holistic services. We offer certification programs that support the ethical practices of Intuitive professionals. Our team of Intuitive Practitioners includes: doctors, psychologists, chiropractor, soul retrievers, mediums, etc who all balance their knowledge with intuitive wisdom.

We want our symbol to be the Blue Morpho Buttefly and the colors on the card to complement it. We want to communicate inspiration, healing and empowerment. Thank you
Updates

Industry/Entity Type

Business

Contact Information for Business Card

Dana Orwick
Medium. Author. Soul Retriever.
Founder, Quiet Harbor

Quiet Harbor

19 North Cedar Mill Drive Suite 100
Fernwood Heights, MI 48517
248-603-7418

www.danaorwick.example

Requirements
Must have
• blue morpho butterfly

```html
<!DOCTYPE html>
<html lang="en">
<head>
<meta charset="utf-8">
<title>Quiet Harbor – Business Card</title>
<link rel="stylesheet" href="https://fonts.googleapis.com/css2?family=Arimo:wght@400;700&display=swap">
<style>
  :root {
    --page-bg: #e6e6e8;
    --card-white: #ffffff;
    --card-black: #0b0b0b;
    --brand-blue: #1f3aa8;
    --morpho-light: #3aa8f0;
    --morpho-deep: #0d4fc4;
    --ink: #111111;
    --muted-grey: #cfcfcf;
  }
  * { box-sizing: border-box; margin: 0; padding: 0; }
  html, body {
    width: 1200px; height: 1000px; overflow: hidden;
    background: var(--page-bg);
    font-family: "Arimo", Arial, sans-serif;
  }
  .sheet {
    position: relative; width: 1200px; height: 1000px;
    display: flex; flex-direction: column; align-items: center;
    justify-content: center; gap: 60px;
  }
  .card {
    position: relative; width: 700px; height: 400px; overflow: hidden;
    background: var(--card-white);
    box-shadow: 0 6px 20px rgba(0,0,0,0.18);
  }

  /* Back of card */
  .card-back .band-blue {
    position: absolute; left: 0; right: 0; top: 262px; height: 58px;
    background: var(--brand-blue);
  }
  .card-back .band-black {
    position: absolute; left: 0; right: 0; top: 320px; bottom: 0;
    background: var(--card-black);
  }
  .card-back .butterfly {
    position: absolute; left: 302px; top: 95px; width: 106px; height: 82px;
  }
  .card-back .brand-name {
    position: absolute; left: 0; right: 0; top: 204px; text-align: center;
    color: var(--brand-blue); font-size: 30px; letter-spacing: 0.5px;
  }
  .card-back .website {
    position: absolute; left: 0; right: 0; top: 276px; text-align: center;
    color: var(--card-white); font-size: 24px; letter-spacing: 1.5px;
  }

  /* Front of card */
  .card-front .header {
    position: absolute; left: 0; right: 0; top: 0; height: 118px;
    background: var(--card-black); padding: 30px 0 0 40px;
  }
  .card-front .person-name {
    color: var(--card-white); font-weight: 700; font-size: 34px;
  }
  .card-front .person-title {
    margin-top: 10px; color: var(--muted-grey); font-size: 18px;
  }
  .card-front .band-blue {
    position: absolute; left: 0; right: 0; top: 118px; height: 48px;
    background: var(--brand-blue); padding-left: 40px;
    color: var(--card-white); font-size: 28px; line-height: 48px;
  }
  .card-front .contact {
    position: absolute; left: 40px; top: 196px; color: var(--ink);
    font-size: 18px; line-height: 1.3;
  }
  .card-front .contact-row { display: flex; align-items: flex-start; gap: 14px; margin-bottom: 14px; }
  .card-front .contact-row svg { flex: none; margin-top: 2px; }
  .card-front .phone-number { font-size: 21px; font-weight: 700; }
  .card-front .butterfly {
    position: absolute; right: 48px; bottom: 50px; width: 120px; height: 92px;
  }
</style>
</head>
<body>
<main class="sheet">

  <section class="card card-back" aria-label="Card back">
    <div class="band-blue"></div>
    <div class="band-black"></div>
    <svg class="butterfly" viewBox="0 0 106 82" role="img" aria-label="Blue morpho butterfly illustration">
      <defs>
        <radialGradient id="morphoBack" cx="50%" cy="45%" r="60%">
          <stop offset="0" stop-color="var(--morpho-light)"/>
          <stop offset="1" stop-color="var(--morpho-deep)"/>
        </radialGradient>
      </defs>
      <rect width="106" height="82" rx="40" fill="url(#morphoBack)"/>
    </svg>
    <div class="brand-name">QUIET HARBOR</div>
    <div class="website">www.danaorwick.example</div>
  </section>

  <section class="card card-front" aria-label="Card front">
    <header class="header">
      <div class="person-name">Dana Orwick</div>
      <div class="person-title">Founder. Author. Soul Retriever</div>
    </header>
    <div class="band-blue">QUIET HARBOR</div>
    <div class="contact">
      <div class="contact-row">
        <svg width="16" height="24" viewBox="0 0 16 24" aria-hidden="true">
          <path d="M8 0C3.6 0 0 3.5 0 7.9 0 13.8 8 24 8 24s8-10.2 8-16.1C16 3.5 12.4 0 8 0zm0 11a3.2 3.2 0 1 1 0-6.4A3.2 3.2 0 0 1 8 11z" fill="var(--ink)"/>
        </svg>
        <div class="address">19 North Cedar Mill Drive Suite 100<br>Fernwood Heights, MI 48517</div>
      </div>
      <div class="contact-row">
        <svg width="22" height="20" viewBox="0 0 22 20" aria-hidden="true">
          <path d="M1 5c0-3 4-4 10-4s10 1 10 4v2h-5V4.5H6V7H1z" fill="var(--ink)"/>
          <path d="M4 9h14l2 10H2z" fill="var(--ink)"/>
          <circle cx="11" cy="14" r="3" fill="var(--card-white)"/>
        </svg>
        <div class="phone-number">248-603-7418</div>
      </div>
    </div>
    <svg class="butterfly" viewBox="0 0 120 92" role="img" aria-label="Blue morpho butterfly illustration">
      <defs>
        <radialGradient id="morphoFront" cx="50%" cy="45%" r="60%">
          <stop offset="0" stop-color="var(--morpho-light)"/>
          <stop offset="1" stop-color="var(--morpho-deep)"/>
        </radialGradient>
      </defs>
      <rect width="120" height="92" rx="44" fill="url(#morphoFront)"/>
    </svg>
  </section>

</main>
</body>
</html>
```